Brantley Advisory Group provides support for renewable energy projects to utilities and suppliers

I need a professional looking business card that is both simple and elegant and unique. My clients are mostly large organizations not individuals. I am a consultant with my own company that is small but would like to give clients the impression I am larger. Smart grid, fiber optics, software, field hardware, distribution automation, substation automation, operations, energy storage/batteries, microgrids, customer service, strategy/roadmaps, conservation, Automated Metering Infrastruture (AMI or smart meters) are all areas of focus.

Target Market(s)

Utilities, suppliers, governmental agencies involved in energy. All types of energy especially natural gas and electrical. Especially renewable energy or green projects.

Contact Information for Business Card

Name - Mark Brantley Cell Phone - 425.318.2746 Email - mbrantley@brantleyag-example.com
Company - Brantley Advisory Group (logo) Title - Principal

Font styles to use
Serif
Sans Serif

Colors

Designer to choose colors to be used in the design.

Requirements
Must have
• Simple and professional and powerful.
• Unique/creative design.
Nice to have
• Utilize color scheme to accent logo colors. Maybe some geometric pattern on edge of card with color.
Should not have
• Busy, complicated, traditional

```html
<!DOCTYPE html>
<html lang="en">
<head>
<meta charset="utf-8">
<title>Brantley Advisory Group – Business Card</title>
<link rel="stylesheet" href="https://fonts.googleapis.com/css2?family=Open+Sans:wght@400;600;700&display=swap">
<style>
  :root {
    --stage: #1e1e1e;
    --card-blue: #1010a0;
    --bright-blue: #2a2ae6;
    --accent-green: #5f8f35;
    --light-green: #9fd85a;
    --white: #ffffff;
    --ink-grey: #6f6f6f;
    --paper: #ffffff;
  }
  * { box-sizing: border-box; margin: 0; padding: 0; }
  html, body {
    width: 1200px; height: 900px; overflow: hidden;
    background: var(--stage);
    font-family: "Open Sans", Arial, sans-serif;
  }
  .card {
    position: absolute; left: 250px;
    width: 700px; height: 400px;
    overflow: hidden;
  }

  /* Front */
  .card-front { top: 40px; background: var(--card-blue); }
  .front-brand {
    position: absolute; left: 60px; top: 140px;
    display: flex; align-items: center; gap: 16px;
  }
  .brand-square {
    width: 30px; height: 30px; flex: none;
    border: 3px solid var(--white); border-radius: 4px;
  }
  .brand-name {
    color: var(--white); font-weight: 700; font-size: 30px;
    letter-spacing: .3px; line-height: 1.15;
  }
  .front-brand .brand-name { max-width: 240px; }
  .pattern-field {
    position: absolute; right: 0; top: 0;
    width: 400px; height: 400px;
    background:
      radial-gradient(closest-side at 50% 48%, rgba(235,240,245,.75), rgba(235,240,245,0) 55%),
      radial-gradient(closest-side at 62% 42%, rgba(159,216,90,.85), rgba(159,216,90,0)),
      radial-gradient(closest-side at 42% 62%, rgba(95,143,53,.9), rgba(95,143,53,0)),
      radial-gradient(closest-side at 58% 50%, rgba(42,42,230,.95), rgba(42,42,230,0));
  }

  /* Back */
  .card-back { top: 470px; background: var(--paper); }
  .back-band {
    position: absolute; inset: 0 0 auto 0; height: 240px;
    background: var(--card-blue);
  }
  .back-brand {
    position: absolute; left: 0; right: 0; top: 92px;
    display: flex; justify-content: center; align-items: center; gap: 14px;
  }
  .back-brand .brand-name { font-size: 28px; }
  .band-rule {
    position: absolute; left: 80px; right: 80px; top: 205px;
    height: 2px; background: var(--accent-green);
  }
  .contact-row {
    position: absolute; top: 285px; left: 0; right: 0;
    display: flex; align-items: center;
  }
  .person {
    width: 300px; text-align: right; padding-right: 18px;
  }
  .person-name {
    color: var(--card-blue); font-weight: 700; font-size: 30px;
    text-transform: uppercase; line-height: 1;
  }
  .person-title { color: var(--ink-grey); font-size: 18px; margin-top: 6px; }
  .divider { width: 2px; height: 60px; background: var(--accent-green); }
  .contacts { padding-left: 18px; list-style: none; }
  .contacts li {
    display: flex; align-items: center; gap: 10px;
    color: var(--ink-grey); font-size: 17px; line-height: 1.55;
  }
  .contacts svg { width: 18px; height: 18px; flex: none; }
</style>
</head>
<body>
  <section class="card card-front">
    <div class="front-brand">
      <span class="brand-square"></span>
      <span class="brand-name">Brantley Advisory Group</span>
    </div>
    <div class="pattern-field" role="img" aria-label="Cluster of overlapping translucent green, white and blue squares"></div>
  </section>

  <section class="card card-back">
    <div class="back-band"></div>
    <div class="back-brand">
      <span class="brand-square"></span>
      <span class="brand-name">Brantley Advisory Group</span>
    </div>
    <div class="band-rule"></div>

    <div class="contact-row">
      <div class="person">
        <p class="person-name">Mark Brantley</p>
        <p class="person-title">Principal</p>
      </div>
      <div class="divider"></div>
      <ul class="contacts">
        <li>
          <svg viewBox="0 0 24 24" fill="none" stroke="#5f8f35" stroke-width="2" stroke-linecap="round" stroke-linejoin="round" aria-hidden="true">
            <path d="M5 3h4l2 5-2.5 1.5a11 11 0 0 0 6 6L16 13l5 2v4a2 2 0 0 1-2 2A16 16 0 0 1 3 5a2 2 0 0 1 2-2z"/>
          </svg>
          425.318.2746
        </li>
        <li>
          <svg viewBox="0 0 24 24" fill="none" stroke="#5f8f35" stroke-width="2" stroke-linejoin="round" aria-hidden="true">
            <rect x="2" y="5" width="20" height="14" rx="1"/>
            <path d="M2 6l10 7 10-7"/>
          </svg>
          mbrantley@brantleyag-example.com
        </li>
      </ul>
    </div>
  </section>
</body>
</html>
```